Accounting Firm

We are a two partner accounting firm. our business name is VELLOR & BRISKETT. We are accountants and business consultants.

We need a stationery design for our letterhead, with compliments slip, business card and envelope.

We'd like clean, professional look. I'm 39 years old and my partner is 60+, so we'd like modern yet elegant design. Dark Navy Blue as a primary colour is preferred.

Thank you.

Hi Guys

No logo.

Thanks

Accounting

• Firm name :VELLOR & BRISKETT
Business Consultants & Accountants
Address: Level 1 Units 5 & 6, 27 Marrow Crescent ASHGROVE SA 5062
Box address: PO Box 318 BRAMLEY SA 5074
telp: +61 8 8194 6027
fax: +61 8 8456 2719

Dominic Vellor, CA
Lucas Briskett, CPA

dominic.vellor@vellorbriskett.example.au
lucas.briskett@vellorbriskett.example.au

Dark Navy Blue as primary colour

```html
<!DOCTYPE html>
<html lang="en">
<head>
<meta charset="utf-8">
<title>Vellor &amp; Briskett — Stationery</title>
<link rel="stylesheet" href="https://fonts.googleapis.com/css2?family=Arimo:wght@400;700&display=swap">
<style>
  :root {
    --navy: #1f1f55;
    --paper: #ffffff;
    --backdrop: #e0e0e6;
    --ink-grey: #6a6a6a;
    --shadow: 0 2px 6px rgba(0, 0, 0, 0.32);
  }
  * { box-sizing: border-box; margin: 0; padding: 0; }
  html, body {
    width: 1200px; height: 726px; overflow: hidden;
    background: var(--backdrop);
    font-family: "Arimo", Arial, sans-serif;
  }
  .sheet { position: relative; width: 1200px; height: 726px; }

  .piece {
    position: absolute;
    background: var(--paper);
    box-shadow: var(--shadow);
    overflow: hidden;
  }

  /* wordmark: firm name set in the text font, plus tagline */
  .wordmark { text-align: center; color: var(--navy); }
  .wordmark__name {
    display: block;
    font-weight: 400;
    letter-spacing: 0.02em;
    white-space: nowrap;
  }
  .wordmark__tagline {
    display: block;
    font-weight: 700;
    text-transform: uppercase;
    letter-spacing: 0.12em;
    white-space: nowrap;
  }
  .wordmark--card .wordmark__name { font-size: 13px; }
  .wordmark--card .wordmark__tagline { font-size: 4.6px; margin-top: 2px; }
  .wordmark--reversed { color: var(--paper); }

  /* business card fronts */
  .card { width: 220px; height: 122px; }
  .card--front-light { left: 86px; top: 66px; }
  .card--front-dark { left: 325px; top: 66px; background: var(--navy); }
  .card--front .wordmark { position: absolute; left: 0; right: 0; top: 51px; }
  .card__web {
    position: absolute; left: 0; right: 0; top: 105px;
    text-align: center; font-size: 6.5px; color: var(--ink-grey);
  }
  .card--front-dark .card__web { color: var(--paper); }

  /* business card backs */
  .card--person-lucas { left: 85px; top: 220px; }
  .card--person-dominic { left: 323px; top: 220px; }
  .card--person .wordmark { position: absolute; left: 0; right: 0; top: 15px; }
  .card__band {
    position: absolute; left: 0; right: 0; top: 48px; height: 26px;
    background: var(--navy); color: var(--paper);
    display: flex; align-items: center; justify-content: center;
    font-size: 7px; font-weight: 700; letter-spacing: 0.03em;
  }
  .card__details {
    position: absolute; left: 0; right: 0; top: 80px;
    text-align: center; font-size: 6.3px; line-height: 7.6px;
    color: var(--ink-grey);
  }

  /* envelope */
  .envelope { left: 28px; top: 397px; width: 588px; height: 255px; }
  .envelope .wordmark { position: absolute; left: 22px; top: 26px; text-align: left; }
  .envelope .wordmark__name { font-size: 19px; }
  .envelope .wordmark__tagline { font-size: 6.5px; margin-top: 3px; padding-left: 18px; }
  .envelope__band {
    position: absolute; left: 0; right: 0; bottom: 0; height: 39px;
    background: var(--navy); color: var(--paper);
    padding: 9px 0 0 23px; font-size: 8.4px; line-height: 9.6px;
  }

  /* letterhead */
  .letterhead { left: 641px; top: 22px; width: 527px; height: 682px; }
  .letterhead .wordmark { position: absolute; left: 0; right: 0; top: 28px; }
  .letterhead .wordmark__name { font-size: 19px; }
  .letterhead .wordmark__tagline { font-size: 6.5px; margin-top: 3px; }
  .letterhead__band {
    position: absolute; left: 0; right: 0; bottom: 0; height: 39px;
    background: var(--navy); color: var(--paper);
    text-align: center; padding-top: 8px;
    font-size: 8.4px; line-height: 10px;
  }
</style>
</head>
<body>
<main class="sheet">

  <section class="piece card card--front card--front-light">
    <div class="wordmark wordmark--card">
      <span class="wordmark__name">VELLOR &amp; BRISKETT</span>
      <span class="wordmark__tagline">Business Consultants &amp; Accountants</span>
    </div>
    <p class="card__web">www.vellorbriskett.example.au</p>
  </section>

  <section class="piece card card--front card--front-dark">
    <div class="wordmark wordmark--card wordmark--reversed">
      <span class="wordmark__name">VELLOR &amp; BRISKETT</span>
      <span class="wordmark__tagline">Business Consultants &amp; Accountants</span>
    </div>
    <p class="card__web">www.vellorbriskett.example.au</p>
  </section>

  <section class="piece card card--person card--person-lucas">
    <div class="wordmark wordmark--card">
      <span class="wordmark__name">VELLOR &amp; BRISKETT</span>
      <span class="wordmark__tagline">Business Consultants &amp; Accountants</span>
    </div>
    <div class="card__band">LUCAS BRISKETT, CPA</div>
    <p class="card__details">
      Level 2 Suite 3, 27 Marrow Crescent ASHGROVE SA 5062<br>
      PO Box 318 BRAMLEY SA 5074<br>
      tel.: +61 8 8194 6027 • fax: +61 8 8456 2719<br>
      lucas.briskett@vellorbriskett.example.au
    </p>
  </section>

  <section class="piece card card--person card--person-dominic">
    <div class="wordmark wordmark--card">
      <span class="wordmark__name">VELLOR &amp; BRISKETT</span>
      <span class="wordmark__tagline">Business Consultants &amp; Accountants</span>
    </div>
    <div class="card__band">DOMINIC VELLOR, CA</div>
    <p class="card__details">
      Level 2 Suite 3, 27 Marrow Crescent ASHGROVE SA 5062<br>
      PO Box 318 BRAMLEY SA 5074<br>
      tel.: +61 8 8194 6027 • fax: +61 8 8456 2719<br>
      dominic.vellor@vellorbriskett.example.au
    </p>
  </section>

  <section class="piece envelope">
    <div class="wordmark">
      <span class="wordmark__name">VELLOR &amp; BRISKETT</span>
      <span class="wordmark__tagline">Business Consultants &amp; Accountants</span>
    </div>
    <p class="envelope__band">
      Level 2 Suite 3, 27 Marrow Crescent ASHGROVE SA 5062<br>
      PO Box 318 BRAMLEY SA 5074
    </p>
  </section>

  <section class="piece letterhead">
    <div class="wordmark">
      <span class="wordmark__name">VELLOR &amp; BRISKETT</span>
      <span class="wordmark__tagline">Business Consultants &amp; Accountants</span>
    </div>
    <p class="letterhead__band">
      Level 2 Suite 3, 27 Marrow Crescent ASHGROVE SA 5062 • PO Box 318 BRAMLEY SA 5074<br>
      tel.: +61 8 8194 6027 • fax: +61 8 8456 2719
    </p>
  </section>

</main>
</body>
</html>
```